Quiet River Psalter Reflections for Every Season of Long Waiting

This is not an Eastern meditation method. No images or themes from guru style or Eastern meditations from Hinduism or Buddhism will work. This is a Biblical Christian-based method. Some sort of Divine Light from Heaven may be the look. Some "ancient scroll" for the title to be written in may work.

```html
<!DOCTYPE html>
<html lang="en">
<head>
<meta charset="utf-8">
<title>Quiet River Psalter — Book Cover</title>
<link rel="stylesheet" href="https://fonts.googleapis.com/css2?family=Bodoni+Moda:wght@400;600&family=Arimo:wght@700&display=swap">
<style>
  :root {
    --page-bg: #e9e9e9;
    --title-red: #e8070c;
    --subtitle-ink: #111111;
    --author-ink: #1a1410;
    --sky-violet: #8a5a8c;
    --sky-rose: #d98a9a;
    --sky-gold: #f6c24a;
    --sky-glow: #fff6d8;
    --sky-amber: #f1a531;
    --dusk-plum: #3a2233;
  }
  * { margin: 0; padding: 0; box-sizing: border-box; }
  html, body {
    width: 1200px;
    height: 800px;
    overflow: hidden;
    background: var(--page-bg);
  }
  .canvas {
    position: relative;
    width: 1200px;
    height: 800px;
  }
  .book-cover {
    position: absolute;
    left: 365px;
    top: 40px;
    width: 470px;
    height: 720px;
    overflow: hidden;
    text-align: center;
  }
  .cover-sky {
    position: absolute;
    inset: 0;
    background:
      radial-gradient(ellipse 38% 26% at 40% 46%, var(--sky-glow) 0%, rgba(255,246,216,0.6) 40%, rgba(255,246,216,0) 100%),
      radial-gradient(ellipse 70% 30% at 55% 78%, rgba(250,230,120,0.85) 0%, rgba(250,230,120,0) 100%),
      linear-gradient(200deg, rgba(90,40,70,0.75) 0%, rgba(90,40,70,0) 28%),
      linear-gradient(20deg, rgba(40,25,30,0.7) 0%, rgba(40,25,30,0) 22%),
      linear-gradient(180deg, var(--sky-violet) 0%, var(--sky-rose) 14%, var(--sky-gold) 48%, var(--sky-amber) 72%, #f4c94c 86%, var(--dusk-plum) 96%, #221520 100%);
  }
  .cover-text {
    position: relative;
    z-index: 1;
    height: 100%;
  }
  .title {
    position: absolute;
    left: 0;
    right: 0;
    top: 88px;
    font-family: "Bodoni Moda", "Didot", serif;
    font-weight: 400;
    color: var(--title-red);
    line-height: 0.9;
  }
  .title-line { display: block; }
  .title-line--large { font-size: 104px; }
  .title-line--small { font-size: 62px; margin: 6px 0 2px; letter-spacing: 1px; }
  .subtitle {
    position: absolute;
    left: 0;
    right: 0;
    top: 490px;
    font-family: "Arimo", Arial, sans-serif;
    font-weight: 700;
    font-size: 19px;
    line-height: 1.4;
    color: var(--subtitle-ink);
  }
  .author {
    position: absolute;
    left: 0;
    right: 0;
    top: 654px;
    font-family: "Bodoni Moda", "Didot", serif;
    font-weight: 400;
    font-size: 25px;
    letter-spacing: 1.5px;
    color: var(--author-ink);
  }
</style>
</head>
<body>
<main class="canvas">
  <section class="book-cover">
    <div class="cover-sky" role="img" aria-label="Photograph of a glowing sunset sky with rays of heavenly light breaking through pink and golden clouds, tree silhouettes at the lower edges"></div>
    <div class="cover-text">
      <h1 class="title">
        <span class="title-line title-line--large">QUIET</span>
        <span class="title-line title-line--large">RIVER</span>
        <span class="title-line title-line--small">PSALTER</span>
      </h1>
      <p class="subtitle">REFLECTIONS FOR EVERY SEASON<br>OF LONG WAITING</p>
      <p class="author">THOMAS WARELEY</p>
    </div>
  </section>
</main>
</body>
</html>
```